Acupuncturist in NYC and Fire Island need cohesive design

I need a new website that is elegant, creative and interesting. A blend of art and science if you will. I have two locations with different feels so I want to somehow merge the two feelings if possible. Perhaps shift the focus to the practitioner and then outline both locations. Specialist in pain/sports conditions and facial rejuvenation with over 20 years experience and esteemed at her craft. Logo now is Calvorian dancer- love it but maybe need to tweak it or redesign.

Need extra days to review

```html
<!DOCTYPE html>
<html lang="en">
<head>
<meta charset="utf-8">
<title>Tidewell Acupuncture</title>
<link rel="stylesheet" href="https://fonts.googleapis.com/css2?family=Krona+One&family=Roboto:wght@400;500;700&display=swap">
<style>
:root{
  --ink:#3d3d3d;
  --ink-soft:#666;
  --charcoal:#555555;
  --tile:#e9e8e8;
  --line:#dcdcdc;
  --white:#ffffff;
  --night:#2b3444;
  --head:"Krona One", sans-serif;
  --body:"Roboto", Arial, sans-serif;
}
*{margin:0;padding:0;box-sizing:border-box}
html,body{width:1200px;height:4662px;overflow:hidden;background:var(--white)}
body{position:relative;font-family:var(--body);color:var(--ink)}
.abs{position:absolute}
.photo{position:absolute}
.heading{font-family:var(--head);color:var(--ink);letter-spacing:2px;text-transform:uppercase}
.btn{position:absolute;display:flex;align-items:center;justify-content:center;font:700 15px var(--body);color:#fff;background:var(--charcoal);border-radius:12px 12px 0 12px}
.btn-outline{position:absolute;display:flex;align-items:center;justify-content:center;font:500 15px var(--body);color:var(--ink);border:2px solid var(--charcoal);border-radius:12px 12px 0 12px;background:transparent}
.center{text-align:center}
.sub{font-size:14.5px;line-height:23px;color:var(--ink-soft)}

/* header */
.site-header{top:0;left:0;width:1200px;height:104px;background:#fff}
.brand{display:flex;align-items:center;gap:10px}
.brand-mark{width:62px;height:62px;border:2px solid #999;border-radius:50%}
.brand-name{font-family:var(--head);font-size:19px;color:var(--ink);line-height:20px}
.brand-name small{display:block;font-size:10px;letter-spacing:7px;color:var(--ink-soft)}
.main-nav a{position:absolute;top:44px;font:500 14px var(--body);letter-spacing:1px;color:var(--ink);text-decoration:none}
.call-box{left:975px;top:0;width:225px;height:104px;background:var(--charcoal);color:#fff;display:flex;align-items:center;gap:14px;padding-left:38px}
.call-box .ring{width:30px;height:30px;border-radius:50%;background:#777;display:flex;align-items:center;justify-content:center}
.call-box p{font-family:var(--head);font-size:12px;line-height:15px;letter-spacing:1px}

/* hero */
.hero{top:104px;left:0;width:1200px;height:499px;background:linear-gradient(90deg,#ececec 0%,#e4e2e0 40%,#e8c9b3 70%,#d9a888 100%)}
.hero h1{position:absolute;left:127px;top:126px;font-size:33px;line-height:44px}

/* about */
.about-title{left:470px;top:748px;font-size:29px;line-height:44px}
.about-text{left:600px;top:868px;width:475px;font-size:13.5px;line-height:23px;color:var(--ink-soft)}
.badge{left:189px;top:1100px;width:157px;height:137px;background:#fff;border:4px solid var(--charcoal);display:flex;flex-direction:column;align-items:center;justify-content:center}
.badge b{font-family:var(--head);font-size:22px;line-height:24px;color:var(--ink)}
.badge span{font:500 17px var(--body);color:var(--ink)}

/* services */
.service{top:1374px;width:300px;height:434px}
.service-card{background:var(--tile);text-align:center}
.service-card .icon{width:76px;height:90px;margin:58px auto 10px;border-radius:38px;background:#d4d2d2}
.service-card h3{font-family:var(--head);font-size:17px;line-height:20px;letter-spacing:2px;color:var(--ink)}
.service-card p{width:240px;margin:20px auto 0;font-size:14px;line-height:22px;color:var(--ink-soft)}

/* gallery */
.section-title{left:0;width:1200px;font-size:30px;text-align:center}
.sub-block{left:270px;width:660px;text-align:center}

/* why */
.why{top:2582px;left:0;width:1200px;height:584px;background:linear-gradient(180deg,#323c4f 0%,#2a3142 55%,#1f2230 100%)}
.why .section-title{color:#fff}
.why .sub{color:#e3e6ec}
.feature{width:240px;text-align:center;color:#fff}
.feature .disc{width:104px;height:104px;margin:0 auto;border-radius:50%;border:2px solid #fff;display:flex;align-items:center;justify-content:center}
.feature h4{margin-top:20px;font:700 16px var(--body)}
.feature p{margin-top:12px;font-size:14px;line-height:20px;color:#e6e8ee}

/* blog */
.post{top:3428px;width:296px;height:342px;border:1px solid var(--line);background:#fff}
.post .thumb{height:182px}
.post h5{margin:20px 22px 0;font:400 19px var(--body);line-height:22px;color:var(--ink-soft)}
.post time{display:block;margin:26px 24px 0;font:700 13px var(--body);color:var(--ink)}

/* locations */
.location{top:3890px;width:600px;height:476px}
.location h3{position:absolute;top:145px;width:600px;text-align:center;font-family:var(--head);font-size:22px;letter-spacing:2px;color:#fff}
.contact-list{position:absolute;top:205px;list-style:none;color:#fff;font-size:16px;line-height:19px}
.contact-list li{display:flex;gap:8px;margin-bottom:18px}
.contact-list svg{flex:none;margin-top:2px}

/* footer */
.footer-nav a{position:absolute;top:4510px;font:500 14px var(--body);letter-spacing:1px;color:var(--ink);text-decoration:none}
.copyright{top:4548px;left:0;width:1200px;text-align:center;font-size:14px;color:var(--ink-soft)}
.social{top:4588px;left:538px;display:flex;gap:12px}
.social span{width:32px;height:32px;border-radius:50%;background:#111}
</style>
</head>
<body>

<header class="abs site-header">
  <div class="abs brand" style="left:62px;top:20px">
    <div class="brand-mark"></div>
    <div class="brand-name">TIDEWELL<small>ACUPUNCTURE</small></div>
  </div>
  <nav class="main-nav">
    <a style="left:400px">HOME</a>
    <a style="left:498px">SERVICES</a>
    <a style="left:631px">WHY US?</a>
    <a style="left:757px">NEWS</a>
    <a style="left:861px">CONTACT</a>
  </nav>
  <div class="abs call-box">
    <div class="ring"><svg width="14" height="14" viewBox="0 0 24 24"><path fill="#fff" d="M6.6 10.8a15 15 0 0 0 6.6 6.6l2.2-2.2c.3-.3.7-.4 1-.2 1.1.4 2.3.6 3.6.6.6 0 1 .4 1 1V20c0 .6-.4 1-1 1A17 17 0 0 1 3 4c0-.6.4-1 1-1h3.5c.6 0 1 .4 1 1 0 1.3.2 2.5.6 3.6.1.3 0 .7-.2 1z"/></svg></div>
    <p>CALL US:<br>888 888 88</p>
  </div>
</header>

<section class="abs hero" role="img" aria-label="Practitioner placing acupuncture needles in a client's shoulder">
  <h1 class="heading">Welcome to<br>Tidewell<br>Acupuncture</h1>
  <a class="btn" style="left:127px;top:279px;width:152px;height:50px">CONTACT US</a>
</section>

<section>
  <div class="photo" style="left:125px;top:742px;width:300px;height:396px;background:linear-gradient(180deg,#8ea9c4 0%,#c9b8a0 45%,#b08a4e 75%,#7d6538 100%)" role="img" aria-label="Lighthouse among beach grass and dunes"></div>
  <div class="photo" style="left:279px;top:868px;width:263px;height:312px;background:#fff"></div>
  <div class="photo" style="left:287px;top:876px;width:247px;height:296px;background:linear-gradient(160deg,#ece8e4 0%,#e2c6b2 55%,#c99c80 100%)" role="img" aria-label="Client receiving facial acupuncture"></div>
  <div class="abs badge"><b>20<br>YEARS</b><span>EXPERIENCE</span></div>
  <h2 class="abs heading about-title">About Tidewell<br>Acupuncture</h2>
  <p class="abs about-text">Sed ut perspiciatis unde omnis iste natus error sit voluptatem accusantium doloremque laudantium, totam rem aperiam, eaque ipsa quae ab illo inventore veritatis et quasi architecto beatae vitae dicta sunt explicabo. Nemo enim ipsam voluptatem quia voluptas sit aspernatur aut odit aut fugit, sed quia consequuntur magni dolores eos qui ratione voluptatem sequi nesciunt. Neque porro quisquam est, qui dolorem ipsum quia dolor sit amet, consectetur, adipisci velit, sed quia non numquam eius modi tempora incidunt ut labore et dolore magnam aliquam quaerat voluptatem.</p>
  <a class="btn" style="left:600px;top:1102px;width:150px;height:50px">READ MORE</a>
</section>

<section>
  <div class="abs service" style="left:0;background:linear-gradient(150deg,#6b4a38 0%,#b27f60 50%,#4a3328 100%)" role="img" aria-label="Massage therapist working on a client's back"></div>
  <div class="abs service service-card" style="left:300px">
    <div class="icon" role="img" aria-label="Line drawing of a spine and shoulders"></div>
    <h3>PAIN/SPORTS<br>CONDITIONS</h3>
    <p>Sed ut perspiciatis unde omnis iste natus error sit voluptatem acc santium doloremque laudantium, totam rem aperiam, eaqu.</p>
    <a class="btn-outline" style="left:82px;top:336px;width:134px;height:42px">READ MORE</a>
  </div>
  <div class="abs service" style="left:600px;background:linear-gradient(160deg,#cfcfcf 0%,#e8d6ca 50%,#a88f82 100%)" role="img" aria-label="Facial treatment with a microneedling pen"></div>
  <div class="abs service service-card" style="left:900px">
    <div class="icon" role="img" aria-label="Line drawing of a face with a needle"></div>
    <h3>FACIAL<br>REJUVENATION</h3>
    <p>Sed ut perspiciatis unde omnis iste natus error sit voluptatem acc santium doloremque laudantium, totam rem aperiam, eaqu.</p>
    <a class="btn-outline" style="left:82px;top:336px;width:134px;height:42px">READ MORE</a>
  </div>
</section>

<section>
  <h2 class="abs heading section-title" style="top:1926px">Our Gallery</h2>
  <p class="abs sub sub-block" style="top:1982px">Sed ut perspiciatis unde omnis iste natus error sit voluptatem accusantium doloremque laudantium, totam rem aperiam, eaque ipsa quae ab illo inventore veritatis et quasi archit</p>
  <div class="photo" style="left:92px;top:2070px;width:242px;height:332px;background:linear-gradient(180deg,#d8c0a8 0%,#7a5640 60%,#3b2a22 100%)" role="img" aria-label="Facial acupuncture session"></div>
  <div class="photo" style="left:350px;top:2070px;width:242px;height:332px;background:linear-gradient(180deg,#eceae6 0%,#e3c4ab 60%,#cfa083 100%)" role="img" aria-label="Needles placed along a client's back"></div>
  <div class="photo" style="left:608px;top:2070px;width:242px;height:332px;background:linear-gradient(180deg,#a9ae9a 0%,#7c6250 55%,#5e4438 100%)" role="img" aria-label="Back massage on a treatment table"></div>
  <div class="photo" style="left:866px;top:2070px;width:242px;height:332px;background:linear-gradient(135deg,#f1efef 0%,#e6b7b0 45%,#d92a2a 100%)" role="img" aria-label="Needles with red heat light on skin"></div>
  <a class="btn" style="left:525px;top:2455px;width:150px;height:50px">VIEW MORE</a>
</section>

<section class="abs why" role="img" aria-label="City skyline at dusk">
  <h2 class="abs heading section-title" style="top:78px">Why Choose Us?</h2>
  <p class="abs sub sub-block" style="top:140px">Sed ut perspiciatis unde omnis iste natus error sit voluptatem accusantium doloremque laudantium, totam rem aperiam, eaque ipsa quae ab illo inventore veritatis et quasi archit</p>
  <div class="abs feature" style="left:106px;top:249px">
    <div class="disc"><svg width="40" height="28" viewBox="0 0 40 28"><rect x="1" y="1" width="38" height="26" rx="3" fill="#fff"/><circle cx="20" cy="14" r="7" fill="#2f3748"/><circle cx="7" cy="14" r="2" fill="#2f3748"/><circle cx="33" cy="14" r="2" fill="#2f3748"/></svg></div>
    <h4>Finibus Bonorum</h4>
    <p>Lorem ipsum dolorsit amet, consectetur adilo piscing elit sed r adilo piscdo.</p>
  </div>
  <div class="abs feature" style="left:355px;top:249px">
    <div class="disc"><svg width="34" height="36" viewBox="0 0 34 36"><circle cx="17" cy="10" r="9" fill="#fff"/><path d="M1 36c0-10 7-15 16-15s16 5 16 15z" fill="#fff"/></svg></div>
    <h4>Finibus Bonorum</h4>
    <p>Lorem ipsum dolorsit amet, consectetur adilo piscing elit sed r adilo piscdo.</p>
  </div>
  <div class="abs feature" style="left:604px;top:249px">
    <div class="disc"><svg width="36" height="36" viewBox="0 0 36 36"><circle cx="18" cy="18" r="17" fill="#fff"/><path d="M18 8v11l7 5" stroke="#2f3748" stroke-width="3" fill="none" stroke-linecap="round"/></svg></div>
    <h4>Finibus Bonorum</h4>
    <p>Lorem ipsum dolorsit amet, consectetur adilo piscing elit sed r adilo piscdo.</p>
  </div>
  <div class="abs feature" style="left:853px;top:249px">
    <div class="disc"><svg width="36" height="34" viewBox="0 0 36 34"><path d="M4 22v-4a14 14 0 0 1 28 0v4" stroke="#fff" stroke-width="3.5" fill="none"/><rect x="2" y="20" width="9" height="13" rx="3" fill="#fff"/><rect x="25" y="20" width="9" height="13" rx="3" fill="#fff"/></svg></div>
    <h4>Finibus Bonorum</h4>
    <p>Lorem ipsum dolorsit amet, consectetur adilo piscing elit sed r adilo piscdo.</p>
  </div>
</section>

<section>
  <h2 class="abs heading section-title" style="top:3276px">Latest Blog Posts</h2>
  <p class="abs sub sub-block" style="top:3336px">Sed ut perspiciatis unde omnis iste natus error sit voluptatem accusantium doloremque laudantium, totam rem aperiam, eaque ipsa quae ab illo inventore veritatis et quasi archit</p>
  <article class="abs post" style="left:127px">
    <div class="thumb" style="background:linear-gradient(150deg,#f3e6e0 0%,#e3bfa7 60%,#c79577 100%)" role="img" aria-label="Relaxing head massage"></div>
    <h5>Lorem ipsum dolor sit amet, consectetur adipis cing elit sed do eius.</h5>
    <time>SEP 27 2023</time>
  </article>
  <article class="abs post" style="left:452px">
    <div class="thumb" style="background:linear-gradient(180deg,#f2f2f0 0%,#e6cdb8 60%,#d8b296 100%)" role="img" aria-label="Woman enjoying a back massage"></div>
    <h5>Lorem ipsum dolor sit amet, consectetur adipis cing elit sed do eius.</h5>
    <time>SEP 27 2023</time>
  </article>
  <article class="abs post" style="left:776px">
    <div class="thumb" style="background:linear-gradient(150deg,#9d9ea4 0%,#b9876a 50%,#4d4a55 100%)" role="img" aria-label="Therapist treating a client's back"></div>
    <h5>Lorem ipsum dolor sit amet, consectetur adipis cing elit sed do eius.</h5>
    <time>SEP 27 2023</time>
  </article>
</section>

<section>
  <div class="abs location" style="left:0;background:linear-gradient(180deg,#5a5f6b 0%,#4a3e36 45%,#2a2622 100%)" role="img" aria-label="New York City skyline at sunset">
    <h3>NYC LOCATION</h3>
    <ul class="contact-list" style="left:185px">
      <li><svg width="12" height="16" viewBox="0 0 12 16"><path d="M6 0a6 6 0 0 0-6 6c0 4.5 6 10 6 10s6-5.5 6-10a6 6 0 0 0-6-6zm0 8.5A2.5 2.5 0 1 1 6 3.5a2.5 2.5 0 0 1 0 5z" fill="#fff"/></svg><span>Lorem Dum street 123 LJD<br>dumy numers 463.</span></li>
      <li><svg width="14" height="14" viewBox="0 0 24 24"><path fill="#fff" d="M6.6 10.8a15 15 0 0 0 6.6 6.6l2.2-2.2c.3-.3.7-.4 1-.2 1.1.4 2.3.6 3.6.6.6 0 1 .4 1 1V20c0 .6-.4 1-1 1A17 17 0 0 1 3 4c0-.6.4-1 1-1h3.5c.6 0 1 .4 1 1 0 1.3.2 2.5.6 3.6.1.3 0 .7-.2 1z"/></svg><span>Phone: 23 456 7890</span></li>
      <li><svg width="14" height="12" viewBox="0 0 14 12"><rect width="14" height="12" rx="1" fill="#fff"/><path d="M1 1l6 5 6-5" stroke="#4a3e36" stroke-width="1.4" fill="none"/></svg><span>Email:info@company.com</span></li>
    </ul>
  </div>
  <div class="abs location" style="left:600px;background:linear-gradient(180deg,#8f8f8f 0%,#a5a5a5 50%,#b3b3b3 100%)" role="img" aria-label="Lighthouse above coastal dunes">
    <h3>FIRE ISLAND LOCATION</h3>
    <ul class="contact-list" style="left:185px">
      <li><svg width="12" height="16" viewBox="0 0 12 16"><path d="M6 0a6 6 0 0 0-6 6c0 4.5 6 10 6 10s6-5.5 6-10a6 6 0 0 0-6-6zm0 8.5A2.5 2.5 0 1 1 6 3.5a2.5 2.5 0 0 1 0 5z" fill="#fff"/></svg><span>Lorem Dum street 123 LJD<br>dumy numers 463.</span></li>
      <li><svg width="14" height="14" viewBox="0 0 24 24"><path fill="#fff" d="M6.6 10.8a15 15 0 0 0 6.6 6.6l2.2-2.2c.3-.3.7-.4 1-.2 1.1.4 2.3.6 3.6.6.6 0 1 .4 1 1V20c0 .6-.4 1-1 1A17 17 0 0 1 3 4c0-.6.4-1 1-1h3.5c.6 0 1 .4 1 1 0 1.3.2 2.5.6 3.6.1.3 0 .7-.2 1z"/></svg><span>Phone: 23 456 7890</span></li>
      <li><svg width="14" height="12" viewBox="0 0 14 12"><rect width="14" height="12" rx="1" fill="#fff"/><path d="M1 1l6 5 6-5" stroke="#999" stroke-width="1.4" fill="none"/></svg><span>Email:info@company.com</span></li>
    </ul>
  </div>
</section>

<footer>
  <div class="abs brand" style="left:465px;top:4408px">
    <div class="brand-mark"></div>
    <div class="brand-name">TIDEWELL<small>ACUPUNCTURE</small></div>
  </div>
  <nav class="footer-nav">
    <a style="left:327px">HOME</a>
    <a style="left:425px">SERVICES</a>
    <a style="left:558px">WHY US?</a>
    <a style="left:684px">NEWS</a>
    <a style="left:788px">CONTACT</a>
  </nav>
  <p class="abs copyright">Copyright © 2023 &nbsp;All Rights Reserved.</p>
  <div class="abs social" aria-label="Social links"><span></span><span></span><span></span></div>
</footer>

</body>
</html>
```